MAPLE Quarters One-Page Inserts

We need TWO one-page insert for a transplant display stand (6"x8"). We have a few furnished apartments and we need to inform our guests about the services available:

Insert #1: Delivery and Pickup Services in the neighborhood (Laundry, Groceries, Restaurants).
Insert #1 Text: "Heading: Pick and Delivery Services in your neighborhood:" Text below it: "1) Laundry Pickup - Call: +9714-382-6047. 2) Groceries Delivery - Call: +9714-382-6047, 3) Restaurants Delivery - Call: +9714-382-6047"

Insert #2: We also need another one-page insert to encourage the guests to enjoy the candles and to make the apartment have a homier feeling.
Insert #2 Text: "Heading: Feel at home. Text below it: "Dim the lights, light up a candle, play nice music, have a relaxing stay."

Target Market(s)

Staynook Users. Apartment Guests. Tourist. Age Group 20 to 60 years old.

Industry/Entity Type

Hotel

Requirements
Must have
• - The Company logo of MAPLE Quarters must be displayed on the upper corner. (Logo attached). The logo should be a single color either white or black (Not red and black or red and white)
• For Insert # 1: Laundry, Groceries, and Breakfast Resturaunts images or icons. The images/icons must be unified and look like from the same family of images/icons.
• For Insert # 2: A romantic candle(s) dinner pictures.
Nice to have
• Not too many colors
• Not too busy
• Simple
• Eye Catchy
Should not have
• Lots of colors
• Too many images
• Too Busy

```html
<!DOCTYPE html>
<html lang="en">
<head>
<meta charset="utf-8">
<title>MAPLE Quarters – Pick and Delivery Services</title>
<link rel="stylesheet" href="https://fonts.googleapis.com/css2?family=Roboto+Condensed:wght@300;400;700;900&display=swap">
<style>
  :root {
    --backdrop: #d9d6d3;
    --paper: #f4f3f1;
    --ink: #1f1f1f;
    --maroon: #7c2f2a;
    --muted: #3a3a3a;
    --art-top: #f0c64a;
    --art-bottom: #e07a3a;
  }
  * { box-sizing: border-box; margin: 0; padding: 0; }
  html, body {
    width: 1200px; height: 984px; overflow: hidden;
    background: var(--backdrop);
    font-family: "Roboto Condensed", "Arial Narrow", sans-serif;
  }
  .insert {
    position: absolute; left: 255px; top: 32px;
    width: 690px; height: 920px;
    background: linear-gradient(160deg, #f7f6f4 0%, var(--paper) 55%, #e9e7e4 100%);
    box-shadow: 0 10px 30px rgba(0,0,0,.18);
    display: flex; flex-direction: column; align-items: center;
    padding-top: 40px;
  }
  .brand {
    display: flex; align-items: center; gap: 14px;
    color: var(--muted);
    font-weight: 300; font-size: 64px; letter-spacing: 3px; line-height: 1;
  }
  .brand-mark { width: 14px; height: 14px; background: var(--muted); }
  .rider-art {
    margin-top: 20px; width: 340px; height: 250px; border-radius: 18px;
    background: linear-gradient(160deg, var(--art-top), var(--art-bottom));
  }
  .headline {
    margin-top: 22px; text-align: center; text-transform: uppercase;
    font-weight: 900; line-height: .95; white-space: nowrap;
  }
  .headline-lead { display: block; color: var(--ink); font-size: 44px; letter-spacing: .5px; }
  .headline-lead .soft { color: #2c2c2c; }
  .headline-main { display: block; color: var(--maroon); font-size: 72px; letter-spacing: .5px; }
  .services { margin-top: 20px; display: flex; flex-direction: column; gap: 14px; width: 440px; }
  .service-label {
    text-align: center; text-transform: uppercase; font-weight: 300;
    font-size: 26px; line-height: 1.1; color: var(--ink); margin-bottom: 4px;
  }
  .service-line { display: flex; align-items: center; gap: 6px; }
  .phone-icon { width: 34px; height: 34px; flex: none; }
  .number-pill {
    flex: 1; height: 50px; border-radius: 6px 14px 14px 6px;
    display: flex; align-items: center; justify-content: center;
    font-weight: 900; font-size: 38px; letter-spacing: .5px;
    background: var(--maroon); color: #fff;
  }
  .number-pill.outlined { background: transparent; color: var(--maroon); border: 3px solid var(--ink); }
  .website {
    margin-top: 24px; font-weight: 700; font-size: 20px; letter-spacing: 5px; color: var(--ink);
  }
</style>
</head>
<body>
  <main class="insert">
    <header class="brand"><span class="brand-mark"></span>MAPLE</header>

    <div class="rider-art" role="img" aria-label="Illustration of a cheerful courier waving while riding a yellow delivery scooter with a box on the back"></div>

    <h1 class="headline">
      <span class="headline-lead"><span class="soft">Pick and</span> Delivery Services in</span>
      <span class="headline-main">Your Neighborhood</span>
    </h1>

    <section class="services">
      <div class="service">
        <p class="service-label">Laundry Pickup</p>
        <div class="service-line">
          <svg class="phone-icon" viewBox="0 0 34 34" aria-hidden="true"><circle cx="17" cy="17" r="15" fill="none" stroke="var(--maroon)" stroke-width="2.5"/><path d="M12 10c1-1 2-1 3 0l1.5 2.5c.5 1 0 1.8-.8 2.3 1 2 2.5 3.5 4.5 4.5.5-.8 1.3-1.3 2.3-.8L25 20c1 1 1 2 0 3-2 2-5 1-8.5-2.5S10 12 12 10z" fill="var(--maroon)"/></svg>
          <div class="number-pill">+9714-382-6047</div>
        </div>
      </div>
      <div class="service">
        <p class="service-label">Groceries Delivery</p>
        <div class="service-line">
          <svg class="phone-icon" viewBox="0 0 34 34" aria-hidden="true"><circle cx="17" cy="17" r="15" fill="none" stroke="var(--maroon)" stroke-width="2.5"/><path d="M12 10c1-1 2-1 3 0l1.5 2.5c.5 1 0 1.8-.8 2.3 1 2 2.5 3.5 4.5 4.5.5-.8 1.3-1.3 2.3-.8L25 20c1 1 1 2 0 3-2 2-5 1-8.5-2.5S10 12 12 10z" fill="var(--maroon)"/></svg>
          <div class="number-pill outlined">+9714-382-6047</div>
        </div>
      </div>
      <div class="service">
        <p class="service-label">Restaurants Delivery</p>
        <div class="service-line">
          <svg class="phone-icon" viewBox="0 0 34 34" aria-hidden="true"><circle cx="17" cy="17" r="15" fill="none" stroke="var(--maroon)" stroke-width="2.5"/><path d="M12 10c1-1 2-1 3 0l1.5 2.5c.5 1 0 1.8-.8 2.3 1 2 2.5 3.5 4.5 4.5.5-.8 1.3-1.3 2.3-.8L25 20c1 1 1 2 0 3-2 2-5 1-8.5-2.5S10 12 12 10z" fill="var(--maroon)"/></svg>
          <div class="number-pill">+9714-382-6047</div>
        </div>
      </div>
    </section>

    <p class="website">www.maplequarters.com</p>
  </main>
</body>
</html>
```